Upscale beer and food event for Colorado non-profit preserving Lieutenant's Lodge

We need an event poster design that may be incorporated into email invitations. We are a non-profit that helps to preserve an iconic historic building in Colorado. This event celebrates all that is Colorado - especially craft beer and our emerging culinary scene. This event is open to the public. It attracts young professionals...age 30 to 40. You can see our past event design which was done in house...we would like to see something more sophisticated. This year we will need a little room build in for sponsors and committee member names but the other elements are similar...pairings, live music, historic venue, special guest Governor Paul Drenwater, The date is Thursday, August 17th, 2017 from 6:00PM to 8:30m. Early bird tickets start at $55 and go up to 75 on July 13th, 2017. Tickets are available at www.rivetonhearth.example. Contact Marissa Plaut at marissa@vlhtrust.

Target Market(s)

Young professionals, beer and food appreciators, historic preservation supporters

Industry/Entity Type

Non Profit

Colors

Designer to choose colors to be used in the design.

Requirements
Must have
• fresh but elegant feel, think beer at a garden party, nice attire. Focus on Colorado - this event is held at Colorado's "white house" - we refer to it as the valley's hearth. Please be sure that it is clear that the event is hosted by and and benefits the Lieutenant's Lodge Heritage Trust. I can get you a logo but it kinda sucks so just be sure to use the non-profit name. Please include a space for presenting sponsor TRELLWICK SAVINGS CO. We would like to be able to add additional sponsor logos as we go.
Nice to have
• image or sketch of the historic Lieutenant's Lodge at the Quarrington mansion...I have lots of images if you need some high res photos or renderings.
Should not have
• grunge graphics, anything political, it should not be too busy...I like a little white space.

```html
<!DOCTYPE html>
<html lang="en">
<head>
<meta charset="utf-8">
<title>Brews and Bites Pairing 2017</title>
<link rel="stylesheet" href="https://fonts.googleapis.com/css2?family=Quicksand:wght@400;500;700&family=Lobster&family=Kaushan+Script&family=Fredoka:wght@600&display=swap">
<style>
  :root {
    --backdrop: #e6e4e0;
    --paper: #f1ece1;
    --paper-edge: #e6dfcf;
    --ink-grey: #6d6b68;
    --ink-brown: #4b3a2d;
    --ink-soft: #5d5047;
    --gold: #f3c64f;
    --gold-edge: #6a5330;
    --sketch-light: #e3ded4;
    --sketch-dark: #a9a39a;
    --band: rgba(255, 255, 255, 0.85);
  }
  * { box-sizing: border-box; margin: 0; padding: 0; }
  html, body { width: 1200px; height: 900px; overflow: hidden; }
  body { background: var(--backdrop); position: relative; font-family: "Quicksand", sans-serif; }

  .poster {
    position: absolute; left: 290px; top: 11px; width: 620px; height: 878px;
    background: radial-gradient(ellipse at 40% 35%, var(--paper) 55%, var(--paper-edge) 100%);
    box-shadow: 0 6px 18px rgba(0,0,0,0.18);
    overflow: hidden;
  }
  .frame { position: absolute; inset: 9px; border: 3px solid var(--ink-soft); pointer-events: none; z-index: 5; }
  .frame-inner { position: absolute; inset: 15px; border: 1px solid var(--ink-soft); pointer-events: none; z-index: 5; }

  .mansion-sketch {
    position: absolute; left: 290px; top: 150px; width: 318px; height: 716px;
    background: linear-gradient(100deg, rgba(241,236,225,0) 0%, var(--sketch-light) 25%, var(--sketch-dark) 100%);
    clip-path: polygon(30% 32%, 75% 8%, 100% 0, 100% 100%, 0 100%, 0 55%);
  }
  .beer-and-fork {
    position: absolute; left: 38px; top: 356px; width: 76px; height: 176px;
    background: linear-gradient(180deg, #f4efe2 0%, #f1cf6a 22%, #e9b73e 100%);
    border-radius: 10px 10px 18px 18px;
  }

  .text { position: absolute; z-index: 3; text-align: center; white-space: nowrap; }
  .kicker { left: 0; width: 600px; top: 26px; font-size: 22px; color: var(--ink-grey); }
  .title { left: 0; width: 614px; top: 72px; font-family: "Lobster", cursive; font-weight: 400; font-size: 64px; color: var(--ink-grey); line-height: 1; }
  .subtitle { left: 0; width: 614px; top: 132px; font-family: "Lobster", cursive; font-size: 42px; color: var(--ink-grey); line-height: 1; }
  .host { left: 27px; width: 400px; top: 196px; font-family: "Kaushan Script", cursive; font-size: 18px; line-height: 25px; color: var(--ink-soft); }

  .rule { position: absolute; height: 0; border-top: 1.5px solid var(--ink-soft); z-index: 3; }
  .rule-host { left: 39px; width: 356px; top: 266px; }

  .guest-label { left: 18px; width: 400px; top: 274px; font-family: "Kaushan Script", cursive; font-size: 23px; color: var(--ink-brown); }
  .guest-name { left: 0; width: 442px; top: 305px; font-family: "Lobster", cursive; font-size: 28px; color: var(--ink-brown); }

  .ticket-label { font-size: 19px; color: var(--ink-brown); font-weight: 500; }
  .ticket-early { left: 120px; width: 230px; top: 360px; }
  .ticket-late { left: 150px; width: 120px; top: 435px; }
  .price {
    position: absolute; z-index: 3; left: 176px; width: 72px; height: 34px;
    background: var(--gold); border: 2px solid var(--gold-edge); border-radius: 18px;
    font-family: "Lobster", cursive; font-size: 25px; line-height: 30px; text-align: center; color: var(--ink-brown);
  }
  .price-early { top: 389px; }
  .price-late { top: 464px; }

  .when { left: 16px; width: 300px; top: 540px; font-family: "Kaushan Script", cursive; font-size: 22px; line-height: 28px; color: var(--ink-brown); }
  .rule-when { left: 96px; width: 124px; top: 636px; border-top-width: 1px; }

  .features { position: absolute; z-index: 3; left: 28px; width: 248px; top: 648px; list-style: none; }
  .features li { font-size: 15px; color: var(--ink-soft); text-align: center; height: 27px; line-height: 27px; font-style: italic; white-space: nowrap; border-bottom: 1px solid var(--ink-soft); }
  .features li:last-child { border-bottom: none; }
  .features strong { font-family: "Fredoka", sans-serif; font-style: normal; font-weight: 600; color: var(--ink-brown); letter-spacing: 0.5px; }

  .sponsors {
    position: absolute; z-index: 4; left: 11px; top: 738px; width: 578px; height: 76px;
    background: var(--band); display: flex; align-items: center; justify-content: space-around; padding: 0 16px;
  }
  .sponsor { font-weight: 700; font-size: 11px; color: var(--ink-brown); text-align: center; line-height: 1.25; max-width: 120px; display: flex; align-items: center; gap: 5px; }
  .sponsor .dot { width: 10px; height: 10px; border-radius: 50%; background: var(--ink-brown); flex: none; }

  .footer { position: absolute; z-index: 4; top: 822px; left: 20px; width: 560px; display: flex; justify-content: space-around; }
  .footer p { font-size: 14px; line-height: 19px; color: var(--ink-brown); text-align: center; }
  .footer strong { font-weight: 700; }
</style>
</head>
<body>
<main class="poster">
  <div class="mansion-sketch" role="img" aria-label="Pencil sketch of the Lieutenant's Lodge at the Quarrington mansion, with columns, porch and flags"></div>
  <div class="frame"></div>
  <div class="frame-inner"></div>

  <p class="text kicker">Join Us For The 2017</p>
  <h1 class="text title">Brews and Bites</h1>
  <p class="text subtitle">pairing</p>
  <p class="text host">Hosted by and benefits<br>the Lieutenant's Lodge Heritage Trust</p>
  <div class="rule rule-host"></div>

  <p class="text guest-label">special guest</p>
  <p class="text guest-name">Governor Paul Drenwater</p>

  <div class="beer-and-fork" role="img" aria-label="Sketch of a tall glass of wheat beer with a fork"></div>

  <p class="text ticket-label ticket-early">Early bird tickets start at:</p>
  <div class="price price-early">$55</div>
  <p class="text ticket-label ticket-late">On July 13th</p>
  <div class="price price-late">$75</div>

  <p class="text when">Thursday,<br>August 17th, 2017<br>From 6:00pm to 8:30pm</p>
  <div class="rule rule-when"></div>

  <ul class="features">
    <li>Over <strong>15</strong> Food and Beer Pairings</li>
    <li>Live Music by <strong>PINE HOLLOW</strong></li>
    <li>Commemorative <strong>TULIP GLASS</strong></li>
  </ul>

  <section class="sponsors" aria-label="Sponsors">
    <div class="sponsor"><span class="dot"></span>Lieutenant's Lodge Heritage Trust</div>
    <div class="sponsor">Summit Culinary Society</div>
    <div class="sponsor">Front Range Brewers Circle</div>
    <div class="sponsor">TRELLWICK SAVINGS CO</div>
  </section>

  <footer class="footer">
    <p><strong>Tickets</strong> are available at:<br>www.rivetonhearth.example</p>
    <p>Contact <strong>Marissa Plaut</strong> at:<br><strong>marissa@vlhtrust</strong></p>
  </footer>
</main>
</body>
</html>
```